HTML Web Design for RivoLink Website

I require a non functioning web design in HTML format.
The website is for an online platform for connecting contract geoscientists with employers looking for short term geologists and geophysicists.
There will be 12 pages plus 3 sub pages of design to complete in total, but for your submission, please provide three pages and one sub page for review. These are to be submitted upon you winning the design contest, and then you can complete the rest of the pages in the days following that.
Please provide your designs for the Home Page, Contractor Profile Page and the Search Page / Search Results List.
Please review my design brief, and mockup of some of the pages carefully. Also, please find attached my logo.
Note, my logo is red, but I do not want a red dominated design, please use red as an accent colour.

Target Market(s)

Geoscientists

Industry/Entity Type

Oil And Gas

Number of Pages Required

5+ page

Requirements
Must have
• HTML format designs
• Submit 3 pages for competition, but further pages after winner is selected
• Professional and modern
Nice to have
• Some red accent
Should not have
• Too much red

```html
<!DOCTYPE html>
<html lang="en">
<head>
<meta charset="utf-8">
<title>RivoLink – Home</title>
<link href="https://fonts.googleapis.com/css2?family=Source+Sans+3:wght@400;600;700&display=swap" rel="stylesheet">
<style>
  :root{
    --stage-top:#3d3d3d;
    --stage-bottom:#262626;
    --white:#ffffff;
    --accent:#f2465f;
    --ink:#2b2b45;
    --nav-ink:#333333;
    --charcoal:#464646;
    --copper:#8c5f44;
    --footer:#555555;
    --footer-dark:#3a3a3a;
    --map-tone:#6a6a6a;
    --panel:#f4f4f4;
    --panel-line:#dddddd;
    --field-line:#cfcfcf;
    --focus:#8fb0f0;
    --orange:#f7a21b;
    --pin:#f4d51c;
  }
  *{box-sizing:border-box;margin:0;padding:0}
  html,body{width:1200px;height:1000px;overflow:hidden}
  body{
    background:linear-gradient(var(--stage-top),var(--stage-bottom));
    font-family:"Source Sans 3",sans-serif;
    position:relative;
  }
  .page{
    position:absolute;left:426px;top:30px;width:348px;height:942px;
    background:var(--white);
    box-shadow:0 0 6px rgba(0,0,0,.6);
    overflow:hidden;
  }
  .page > *{position:absolute;left:0;width:348px}
  .abs{position:absolute}

  /* header */
  .site-header{top:0;height:35px;background:var(--white)}
  .brand{left:28px;top:6px;font-size:13px;font-weight:700;color:var(--accent);letter-spacing:.2px}
  .main-nav{left:110px;top:15px;display:flex;gap:7px;font-size:4.2px;color:var(--nav-ink);text-transform:uppercase}
  .main-nav .active{color:var(--accent)}
  .header-divider{left:238px;top:6px;width:1px;height:24px;background:#e4e4e4}
  .help-note{left:249px;top:8px;font-size:3.6px;color:#444}
  .chat-btn{left:249px;top:17px;width:30px;height:10px;background:var(--accent);color:var(--white);font-size:3.6px;display:flex;align-items:center;justify-content:center}
  .phone{left:289px;top:18px;font-size:6.4px;color:#333}

  /* hero */
  .hero{top:35px;height:197px;background:linear-gradient(#4a3a3a 0%,#8a5e52 45%,#9c6a55 62%,#3a2a26 78%,#1e1a19 100%)}
  .hero h1{position:absolute;left:0;width:348px;top:50px;text-align:center;color:var(--white);font-weight:400;font-size:17px}
  .join-btn{left:136px;top:100px;width:76px;height:25px;background:var(--accent);color:var(--white);font-size:8px;display:flex;align-items:center;justify-content:center}

  /* registration */
  .register{top:232px;height:162px;display:flex}
  .register-card{width:174px;height:162px;position:relative;color:var(--white);text-align:center}
  .register-card.contractor{background:var(--charcoal)}
  .register-card.employer{background:var(--copper)}
  .register-icon{position:absolute;top:34px;height:30px;background:rgba(255,255,255,.85);border-radius:3px}
  .register-card h2{position:absolute;left:0;width:174px;font-weight:400;font-size:8.5px}
  .register-card p{position:absolute;left:36px;width:102px;font-size:3.5px;line-height:5px}
  .outline-btn{position:absolute;width:39px;height:13px;border:1px solid var(--white);font-size:4.2px;display:flex;align-items:center;justify-content:center}

  /* login */
  .login{top:394px;height:318px}
  .section-title{position:absolute;left:0;width:348px;text-align:center;font-weight:400;font-size:12px;color:var(--ink)}
  .signin-box{left:107px;top:48px;width:134px;height:95px;background:var(--panel);border:1px solid var(--panel-line)}
  .signin-box .box-title{position:absolute;top:5px;width:132px;text-align:center;font-size:7px;color:#444}
  .signin-box .rule{position:absolute;top:17px;left:0;width:132px;height:1px;background:var(--panel-line)}
  .field{position:absolute;left:7px;width:120px;height:16px;background:var(--white);border:1px solid var(--field-line);border-radius:2px;font-size:4px;color:#999;padding:5px 4px}
  .field.focus{border-color:var(--focus)}
  .remember{position:absolute;left:7px;top:72px;font-size:3.4px;color:#777;display:flex;align-items:center;gap:2px}
  .remember i{width:4px;height:4px;border:0.5px solid #999;border-radius:50%}
  .signin-btn{position:absolute;left:95px;top:71px;width:32px;height:13px;background:linear-gradient(#ffb23a,var(--orange));border-radius:2px;color:#5a3300;font-size:4.5px;display:flex;align-items:center;justify-content:center}
  .forgot{left:0;top:150px;text-align:center;font-size:3.6px;color:#555}
  .how-text{left:29px;top:266px;width:292px;font-size:6.8px;line-height:8.4px;color:var(--ink)}

  /* pricing band */
  .pricing{top:712px;height:68px;background:var(--copper);color:var(--white)}
  .pricing h3{position:absolute;left:52px;top:23px;font-weight:400;font-size:9px}
  .pricing p{position:absolute;left:52px;top:35px;font-size:4px}
  .pricing-btn{left:237px;top:23px;width:58px;height:22px;background:var(--accent);border:1px solid #f77;font-size:4.4px;display:flex;align-items:center;justify-content:center}

  /* footer */
  .site-footer{top:780px;height:130px;background:var(--footer);color:var(--white)}
  .world-map{left:29px;top:20px;width:200px;height:100px;background:var(--map-tone);border-radius:40px 30px 50px 20px;opacity:.8}
  .map-pin{left:64px;top:51px;width:10px;height:16px}
  .map-label{left:66px;top:64px;font-size:3.6px;color:var(--pin)}
  .footer-nav{left:240px;width:78px;top:34px;text-align:right;font-size:3.8px;line-height:9px}
  .footer-nav h4{font-weight:400;font-size:5px;margin-bottom:4px}
  .social{left:295px;top:99px;display:flex;gap:5px}
  .social i{width:4px;height:4px;border-radius:50%;background:var(--pin)}
  .back-top{left:240px;width:78px;top:118px;text-align:right;font-size:3.4px}
  .legal{top:910px;height:32px;background:var(--footer-dark);color:var(--white);font-size:3.6px;text-align:center;padding-top:13px}
</style>
</head>
<body>
<div class="page">

  <header class="site-header">
    <div class="abs brand">RivoLink</div>
    <nav class="abs main-nav"><span class="active">Home</span><span>About</span><span>Pricing</span><span>Service</span><span>Contact</span></nav>
    <div class="abs header-divider"></div>
    <div class="abs help-note">Do you need help ? Just Email, Live chat or Call us</div>
    <div class="abs chat-btn">Live Chat</div>
    <div class="abs phone">555.010.0420</div>
  </header>

  <section class="hero" role="img" aria-label="Photograph of oil pumpjacks silhouetted against a dusk sky">
    <h1>Contract Geoscientists Worldwide</h1>
    <div class="abs join-btn">Join Free Today</div>
  </section>

  <section class="register">
    <div class="register-card contractor">
      <div class="register-icon" role="img" aria-label="Icon of three workers in hard hats" style="left:53px;width:68px"></div>
      <h2 style="top:73px">Register as a Contractor</h2>
      <p style="top:84px">Find short-term geology and geophysics projects with operators worldwide. Build your profile, list your skills and availability, and receive contract offers directly.</p>
      <div class="outline-btn" style="left:65px;top:113px">Register</div>
    </div>
    <div class="register-card employer">
      <div class="register-icon" role="img" aria-label="Icon of three business people" style="left:62px;width:50px"></div>
      <h2 style="top:75px">Register as an Employer</h2>
      <p style="top:86px">Post short-term roles for geologists and geophysicists. Search verified profiles, compare rates and experience, and hire qualified contractors for your next project.</p>
      <div class="outline-btn" style="left:66px;top:114px">Register</div>
    </div>
  </section>

  <section class="login">
    <h2 class="section-title" style="top:16px">login for existing members</h2>
    <div class="abs signin-box">
      <div class="box-title">Sign In</div>
      <div class="rule"></div>
      <div class="field focus" style="top:23px">name</div>
      <div class="field" style="top:45px">password</div>
      <div class="remember"><i></i>Remember me</div>
      <div class="signin-btn">Sign In</div>
    </div>
    <div class="abs forgot" style="width:348px">Forgot your password?</div>

    <h2 class="section-title" style="top:204px">How it Works</h2>
    <p class="abs how-text">A text description plus stylized graphics describing how the process works, with a "Join free today" button floating at the side. That button takes the member to the same process as described above. This page also contains the FAQ section below the primary description</p>
  </section>

  <section class="pricing">
    <h3>Do you want to view Plans &amp; Pricing ?</h3>
    <p>Follow the button in the right section.</p>
    <div class="abs pricing-btn">Plans &amp; Pricing</div>
  </section>

  <footer class="site-footer">
    <div class="abs world-map" role="img" aria-label="Dotted world map"></div>
    <svg class="abs map-pin" viewBox="0 0 10 16" aria-hidden="true">
      <path d="M5 0a5 5 0 0 0-5 5c0 4 5 11 5 11s5-7 5-11a5 5 0 0 0-5-5z" fill="#f4d51c"/>
      <circle cx="5" cy="5" r="2" fill="#555"/>
    </svg>
    <div class="abs map-label">USA</div>
    <nav class="abs footer-nav">
      <h4>Navigation</h4>
      <div>Home</div><div>About</div><div>Pricing</div><div>Service</div><div>Contact</div>
    </nav>
    <div class="abs social"><i></i><i></i><i></i></div>
    <div class="abs back-top">Back to Top</div>
  </footer>

  <div class="legal">Copyright 2017 USA by RivoLink</div>
</div>
</body>
</html>
```